Letterhead and Comps Slip Design Project

Letterhead and Compliments Slip for our company in line with our branding in particular our current business card design. 'BrightQuill' is and advertising sales specialist. We want the stationary to incorporate our logo and the colour blue.

Our business card design used blue well and the designer also created a subtle watermark effect with our logo on the front that I think could also be used in the design.

Target Market(s)

Business to business sales - professional look important

Industry/Entity Type

Advertising

Requirements
Must have
• Logo (uploaded), similar look/feel to business card design(uploaded), use of blue and watermark effect.

These details:
BrightQuill Pty Ltd
ABN 52 408 917 363

Office
The Lanternhall
Suite 4&5, 41-57 Orwell St
Surry Hills
NSW 2010

Phone
1300 647 218

International
+61 2 7319 6682

Fax
+61 2 6238 1497

Email
info@brightquill.example.com.au

Web
www.brightquill.example.com.au

```html
<!DOCTYPE html>
<html lang="en">
<head>
<meta charset="utf-8">
<title>BrightQuill Stationery</title>
<link href="https://fonts.googleapis.com/css2?family=Questrial&family=Jost:wght@400;500&family=Allura&display=swap" rel="stylesheet">
<style>
  :root {
    --backdrop: #e6e3df;
    --paper: #ffffff;
    --paper-shade: #f1f1f2;
    --navy: #2e3466;
    --brand-blue: #2a6fd1;
    --ink: #1f1f22;
    --watermark: #ececed;
  }
  html, body {
    margin: 0;
    padding: 0;
    width: 1200px;
    height: 751px;
    overflow: hidden;
    background: var(--backdrop);
  }
  .canvas {
    position: relative;
    width: 1200px;
    height: 751px;
  }
  .sheet {
    position: absolute;
    overflow: hidden;
    background: radial-gradient(ellipse at 30% 20%, var(--paper) 40%, var(--paper-shade) 100%);
    box-shadow: 0 2px 6px rgba(0,0,0,0.18);
  }
  .letterhead { left: 55px; top: 55px; width: 510px; height: 658px; }
  .comp-slip { left: 607px; top: 275px; width: 546px; height: 237px; }

  .watermark {
    position: absolute;
    border-radius: 50%;
    border: 34px solid var(--watermark);
  }
  .letterhead .watermark { left: 285px; top: 355px; width: 330px; height: 330px; }
  .comp-slip .watermark { left: 405px; top: 40px; width: 200px; height: 200px; border-width: 24px; }

  .brand {
    position: absolute;
    display: flex;
    align-items: center;
    gap: 8px;
    font-family: "Questrial", sans-serif;
    color: var(--ink);
  }
  .brand-dot {
    border-radius: 50%;
    background: var(--brand-blue);
  }
  .letterhead .brand { left: 172px; top: 36px; font-size: 24px; }
  .letterhead .brand-dot { width: 40px; height: 40px; }
  .comp-slip .brand { left: 22px; top: 32px; font-size: 24px; }
  .comp-slip .brand-dot { width: 44px; height: 44px; }

  .greeting {
    position: absolute;
    right: 26px;
    top: 42px;
    font-family: "Allura", cursive;
    font-size: 22px;
    color: var(--ink);
  }

  .tab {
    position: absolute;
    width: 9px;
    background: var(--navy);
    border-radius: 1px;
  }
  .letterhead .tab { top: 564px; height: 72px; }
  .comp-slip .tab { top: 174px; height: 54px; }
  .tab.left { left: 0; }
  .tab.right { right: 0; }

  .contact {
    position: absolute;
    left: 0;
    right: 0;
    text-align: center;
    font-family: "Jost", sans-serif;
    font-size: 8.6px;
    line-height: 15px;
    color: var(--ink);
  }
  .contact p { margin: 0; }
  .contact .label { font-weight: 500; color: var(--navy); }
  .letterhead .contact { top: 578px; }
  .letterhead .abn { margin-top: 4px; }
  .comp-slip .contact { top: 187px; font-size: 8.4px; line-height: 13px; }
</style>
</head>
<body>
<main class="canvas">
  <section class="sheet letterhead" aria-label="Letterhead">
    <div class="watermark" aria-hidden="true"></div>
    <div class="brand"><span class="brand-dot"></span><span class="brand-name">BrightQuill</span></div>
    <span class="tab left"></span>
    <span class="tab right"></span>
    <div class="contact">
      <p><span class="label">P.</span> 1300 647 218 /+61 2 7319 6682(International) <span class="label">F.</span> + 61 2 6238 1497 <span class="label">E.</span> info@brightquill.example.com.au</p>
      <p><span class="label">W.</span> www.brightquill.example.com.au | The Lanternhall, Suite 4&amp;5, 41-57 Orwell St, Surry Hills, NSW 2010</p>
      <p class="abn">ABN 52 408 917 363</p>
    </div>
  </section>

  <section class="sheet comp-slip" aria-label="Compliments slip">
    <div class="watermark" aria-hidden="true"></div>
    <div class="brand"><span class="brand-dot"></span><span class="brand-name">BrightQuill</span></div>
    <p class="greeting">With Best Complements</p>
    <span class="tab left"></span>
    <span class="tab right"></span>
    <div class="contact">
      <p>P. 1300 647 218 /+61 2 7319 6682(International) F. + 61 2 6238 1497 E. info@brightquill.example.com.au W. www.brightquill.example.com.au</p>
      <p>The Lanternhall, Suite 4&amp;5, 41-57 Orwell St, Surry Hills, NSW 2010</p>
    </div>
  </section>
</main>
</body>
</html>
```